Norvell Property Services LLC. Commercial & Residential

PROFESSIONAL WINDOW WASHING! professional dryer vent cleaning (prevent fires, $aves money, Lowers your electric bill, save your dryer, less drying time, ask how!)gutter clean outs and tune-up *Lowest Price Quotes Guaranteed!Straightforward Consultancy and Advice to empower homeowners and find solutions that fit your budget!non pressure house cleaning "no pressure...No Damage!Interior & Exterior House Painting call for free in-home consultationPre & Post Tenant Clean-Up PaintGenerator Maintenance Comprehensive Landlord Services & REO (special requests considered) no job too small)!

I would like my business cards to be as professional as possible. I provide property services to commercial and residential clients and need these cards to draw attention and catch ones eye. I have never had business cards for this the services I provide. And I need them so that business owners will trust that our services are the best and also homeowners will call based on the information they see on these cards., I want the window washing service to be the main focal point because it the main service provided. thank you Added Saturday, July 4, 2015

Target Market(s)

Property Services and professional window cleaning highlighted on the front of card rounded edges for card and sleek eye catching cards thank you

Industry/Entity Type

Property Maintenance

Contact Information for Business Card

518-555-0147 Direct. norvellpropertyservicesllc@brindlemail.net

Requirements
Must have
• Professional appearance and eye catch design Property Services as a general point with professional window washing as a highlighted service and all the rest of the services on back of card
Nice to have
• vivid colors but professional appearance

```html
<!DOCTYPE html>
<html lang="en">
<head>
<meta charset="utf-8">
<title>Norvell Property Services – Business Card</title>
<link rel="stylesheet" href="https://fonts.googleapis.com/css2?family=Parisienne&family=Yanone+Kaffeesatz:wght@300;400;600&family=Libre+Baskerville:ital,wght@0,700;1,400&display=swap">
<style>
  :root {
    --page: #ffffff;
    --card: #f3f5c9;
    --swoosh: #c9c903;
    --oval: #ffffff;
    --violet: #6f3fb3;
    --violet-deep: #4b1f7a;
    --accent-flower: #7b4fb6;
  }
  * { margin: 0; padding: 0; box-sizing: border-box; }
  html, body { width: 1200px; height: 686px; overflow: hidden; background: var(--page); }
  .card { position: relative; width: 1200px; height: 686px; }
  .card-art { position: absolute; inset: 0; width: 1200px; height: 686px; }
  .brand-title {
    position: absolute; left: 30px; top: 178px;
    font-family: "Parisienne", cursive; font-weight: 400; font-size: 43px; color: var(--violet-deep);
    white-space: nowrap;
  }
  .tagline {
    position: absolute; left: 90px; width: 500px; text-align: center;
    font-family: "Libre Baskerville", serif; font-weight: 700;
    font-size: 26px; letter-spacing: 11px; color: var(--violet); line-height: 1;
  }
  .tagline-1 { top: 398px; }
  .tagline-2 { top: 438px; left: 92px; width: 510px; }
  .contact-name {
    position: absolute; left: 102px; top: 552px;
    font-family: "Libre Baskerville", serif; font-style: italic;
    font-size: 28px; color: var(--violet);
  }
  .services {
    position: absolute; left: 700px; top: 62px;
    font-family: "Yanone Kaffeesatz", sans-serif; font-weight: 300; font-style: italic;
    font-size: 27px; color: var(--violet); list-style: none; line-height: 42px;
  }
  .services-lead { text-decoration: underline; }
  .services-focus {
    font-weight: 600; font-style: normal; font-size: 30px;
    letter-spacing: 1px; color: var(--violet-deep); text-transform: uppercase;
  }
  .contact {
    position: absolute; left: 700px; top: 334px;
    font-family: "Yanone Kaffeesatz", sans-serif; font-weight: 300; font-style: italic;
    font-size: 27px; color: var(--violet); line-height: 48px;
  }
  .brand-mark {
    position: absolute; left: 828px; top: 466px; width: 172px; height: 166px;
    display: flex; flex-direction: column; align-items: center; justify-content: center; gap: 8px;
  }
  .brand-mark-dot { width: 48px; height: 48px; border-radius: 50%; background: var(--violet); }
  .brand-mark-name {
    font-family: "Yanone Kaffeesatz", sans-serif; font-weight: 400;
    font-size: 24px; color: var(--violet); text-align: center; line-height: 1.05;
  }
</style>
</head>
<body>
<main class="card">
  <svg class="card-art" viewBox="0 0 1050 600">
    <defs>
      <clipPath id="card-shape"><rect x="30" y="30" width="990" height="540" rx="52"/></clipPath>
      <radialGradient id="bloom-fill" cx="0.5" cy="0.5" r="0.5">
        <stop offset="0" stop-color="#dfe48a"/>
        <stop offset="1" stop-color="#e8eba8"/>
      </radialGradient>
    </defs>
    <rect class="card-base" x="30" y="30" width="990" height="540" rx="52" fill="var(--card)"/>
    <g clip-path="url(#card-shape)">
      <ellipse role="img" aria-label="Large pale decorative flower" cx="1010" cy="400" rx="140" ry="230" fill="url(#bloom-fill)" opacity="0.8"/>
    </g>
    <path class="swoosh" d="M0,128 C130,78 400,92 500,140 C470,245 330,312 200,312 C110,312 40,292 0,272 Z" fill="var(--swoosh)"/>
    <ellipse class="title-oval" cx="212" cy="188" rx="220" ry="76" fill="var(--oval)"/>
    <circle role="img" aria-label="Small purple decorative flower" cx="100" cy="88" r="38" fill="var(--accent-flower)"/>
  </svg>

  <h1 class="brand-title">Norvell Property Services</h1>

  <p class="tagline tagline-1">PROFESSIONAL</p>
  <p class="tagline tagline-2">HOME CONSULTANT</p>

  <p class="contact-name">Maren</p>

  <ul class="services">
    <li class="services-lead">For your:</li>
    <li class="services-focus">Professional Window Washing</li>
    <li>Interior &amp; Exterior House Painting</li>
    <li>Pre &amp; Post Tenant Clean-Up Paint</li>
    <li>Generator Maintenance</li>
    <li>Non Pressure House Cleaning</li>
  </ul>

  <div class="contact">
    <p class="contact-phone">Phone: 518-555-0147</p>
    <p class="contact-email">E-mail: norvellpropertyservicesllc@brindlemail.net</p>
  </div>

  <div class="brand-mark">
    <span class="brand-mark-dot"></span>
    <span class="brand-mark-name">Norvell Property<br>Services</span>
  </div>
</main>
</body>
</html>
```